BrightHarbor logo and website profile

BrightHarbor is a newly started business angel network investing in entrepreneurs and start-ups. We need a smart looking logo and website design (based on Wordpress).
The aim of the site is to attract 2 customer segments;
1) Entrepreneurs and start-ups looking for investors
2) Investors/ business angels looking to become part of a larger network of investors for better access to investments
A successful conversion on the website would be for the entrepreneur or investor sending us an e-mail to submit their investment proposal, inquire about our services or ask to join the network of investors.
The website should focus on presenting Bright Harbor and our offerings towards the 2 customer segments. This is NOT a platform like e.g. quillfund.co.
Sites we like;
http://demo.pexorit.net/themes/marigold/agency/
http://www.tallbirchadvisory.no (it's a bit bleak - needs a little more color)
Hi all,
Reason: Been asked to extend by designers still working in their proposals.
Target Market(s)
Two target markets; 1) entrepreneurs looking for investors 2) business angels looking for investment opportunities
Industry/Entity Type
Investment
Requirements
Must have
- The keywords we want associated with our brand are;
Innovation – Integrity – Knowledgeable – Growth – Entrepreneurship
Logodesign (symbol and smart presentation of the company name - bright harbor, both with and without .com)
Wordpress design, pages we need:
- landing page with clear CTA for entrepreneurs and clear CTA for investors
- Portfolio overview of investments made
- General page for our approach, services etc
- Contact us page
- Favicon
- News
- Header/footer information
Other functionality we need;
- Social media integration
The design must support mobile and iPads as well.
We like: less is more :)

```html
<!DOCTYPE html>
<html lang="en">
<head>
<meta charset="utf-8">
<title>Bright Harbor — Logo and Website</title>
<link href="https://fonts.googleapis.com/css2?family=Titillium+Web:wght@300;400;600;700&display=swap" rel="stylesheet">
<style>
:root{
  --blue:#2b7fd6;
  --blue-deep:#3a6d96;
  --slate:#3c4a55;
  --ink:#6f6f6f;
  --ink-soft:#8a8a8a;
  --line:#e2e2e2;
  --green:#2ba52b;
  --amber:#e0a314;
  --red:#c2111f;
  --paper:#fcfcfc;
}
*{box-sizing:border-box;margin:0;padding:0}
html,body{width:1200px;height:1000px;overflow:hidden}
body{font-family:"Titillium Web",Arial,sans-serif;color:var(--ink);background:linear-gradient(#ffffff,#dcdcdc);position:relative}
.abs{position:absolute}

/* brand presentation */
.brand-mark-large{left:150px;top:215px;width:130px;height:130px;background:var(--blue);}
.brand-lockup{left:58px;top:470px;display:flex;align-items:center;gap:14px}
.brand-lockup .dot{width:58px;height:40px;background:var(--blue)}
.brand-lockup .dot{width:40px;height:40px}
.brand-lockup .name{font-size:31px;font-weight:700;color:#8c8c8c;letter-spacing:.5px}

/* site */
.site{left:447px;top:12px;width:738px;height:976px;background:var(--paper)}
.topbar{left:0;top:0;width:738px;height:9px;background:var(--blue-deep)}
.search-tab{left:546px;top:9px;width:25px;height:12px;background:var(--blue-deep);border-radius:0 0 3px 3px}
.site-logo{left:158px;top:36px;display:flex;align-items:center;gap:8px}
.site-logo .dot{width:16px;height:16px;background:var(--blue)}
.site-logo .name{font-size:12px;font-weight:700;color:#7a7a7a}
.nav{left:366px;top:36px;display:flex;font-size:6.5px;color:#777;text-transform:uppercase}
.nav a{display:block;height:37px;padding:6px 7px 0;text-decoration:none;color:inherit}
.nav a.active{background:#ededed;border-bottom:2px solid var(--blue);width:30px;padding-left:6px}

.hero{left:0;top:73px;width:738px;height:198px;background:radial-gradient(circle at 400px 40px,#8b98a2 0,#55626c 30%,#3a4650 70%)}
.hero-title{left:162px;top:156px;color:#fff;font-size:16px;line-height:16px;font-weight:400}
.hero-title b{font-weight:700}
.btn{background:var(--blue);color:#fff;text-align:center}
.hero-btn{left:162px;top:197px;width:90px;height:21px;font-size:9px;line-height:21px}

.welcome-h{left:162px;top:294px;font-size:17px;line-height:16px;font-weight:300;color:#777}
.welcome-h b{font-weight:700}
.body-s{font-size:7.5px;line-height:10.5px;color:#888}
.more{font-size:7px;font-weight:700;color:var(--blue)}
.vrule{left:293px;top:286px;width:1px;height:130px;background:var(--line)}
.card-img{height:57px;background:linear-gradient(90deg,#d7d7d7,#9a9a9a)}
.card-band{color:#fff;font-size:8.5px;line-height:10px;font-weight:700;padding:5px 6px}
.card-band span{font-weight:400}
.connect{left:418px;top:301px;width:44px;height:44px;border-radius:50%;background:var(--red);border:2px solid #fff;color:#fff;font-size:6.5px;font-weight:700;line-height:8px;text-align:center;padding-top:13px}
.hrule{left:150px;width:439px;height:1px;background:var(--line)}

.sec-h{font-size:16px;font-weight:700;color:#7a7a7a}
.pager{display:flex;gap:1px}
.pager i{display:block;width:13px;height:13px;background:#777;color:#fff;font-style:normal;font-size:8px;line-height:13px;text-align:center}
.pager i+i{background:#c8c8c8}
.port-box{top:437px;width:62px;height:56px;border:1px solid #e8e8e8;background:#fff;display:flex;align-items:center;justify-content:center;text-align:center;font-size:7px;font-weight:700;color:#6a6a6a}

.why-h{left:0;width:738px;top:550px;text-align:center;font-size:17px;font-weight:300;color:#777}
.why-h b{font-weight:600}
.feature{top:576px;width:96px}
.feature .icon{width:62px;height:62px;border-radius:50%;background:var(--blue);margin-left:17px;display:flex;align-items:center;justify-content:center}
.feature h3{margin-top:8px;font-size:8.5px;font-weight:700;color:var(--blue);white-space:nowrap}
.feature p{margin-top:3px;font-size:7.5px;line-height:10.5px;color:#888}

.cta-shadow{left:198px;top:737px;width:342px;height:14px;background:radial-gradient(ellipse at 50% 0,rgba(0,0,0,.12),transparent 70%)}
.cta{left:308px;top:738px;display:flex;height:22px}
.cta .label{width:100px;font-size:10px;line-height:22px}
.cta .go{width:22px;background:var(--slate);display:flex;align-items:center;justify-content:center}

.news-img{left:162px;top:831px;width:114px;height:62px;background:linear-gradient(135deg,#d8774a,#6d5a50 50%,#c9c2b8)}
.news-title{left:285px;top:831px;font-size:9px;font-weight:700;color:#444}
.bubble{left:453px;top:831px;width:123px;height:47px;background:#ececec;border-radius:5px;padding:8px 10px;font-size:6.5px;line-height:9px;color:#666}
.bubble:after{content:"";position:absolute;left:9px;bottom:-7px;border:4px solid transparent;border-top:4px solid #ececec;border-left:4px solid #ececec}
.author{left:474px;top:882px;font-size:6.5px;color:#555}
.author span{color:var(--blue)}

.footer{left:0;top:932px;width:738px;height:44px;background:var(--slate)}
.footer .copy{position:absolute;left:162px;top:16px;font-size:6px;color:#fff}
.social{position:absolute;left:533px;top:15px;display:flex;gap:5px}
.social span{width:10px;height:10px;background:#fff;border-radius:1px}
</style>
</head>
<body>

<div class="abs brand-mark-large" role="img" aria-label="Bright Harbor symbol area"></div>
<div class="abs brand-lockup"><span class="dot"></span><span class="name">BRIGHT HARBOR</span></div>

<div class="abs site">
  <div class="abs topbar"></div>
  <div class="abs search-tab">
    <svg width="25" height="12" viewBox="0 0 25 12"><circle cx="12" cy="5.5" r="2" fill="none" stroke="#fff" stroke-width="1"/><line x1="13.5" y1="7" x2="15" y2="8.5" stroke="#fff" stroke-width="1"/></svg>
  </div>

  <div class="abs site-logo"><span class="dot"></span><span class="name">BRIGHT HARBOR</span></div>
  <nav class="abs nav">
    <a class="active">Home</a><a>About us</a><a>Entrepreneurs</a><a>Investors</a><a>Contact</a>
  </nav>

  <div class="abs hero" role="img" aria-label="Businessman touching a glowing network of connected contact icons"></div>
  <h1 class="abs hero-title">You can <b>Connect</b> with<br>and <b>Invest</b></h1>
  <div class="abs btn hero-btn">Learn More</div>

  <h2 class="abs welcome-h">Welcome to<br><b>Bright Harbor</b></h2>
  <p class="abs body-s" style="left:162px;top:334px;width:122px">BrightHarbor is a newly started business angel network investing in entrepreneurs and start-ups.</p>
  <div class="abs more" style="left:162px;top:374px">READ MORE</div>
  <div class="abs vrule"></div>

  <div class="abs" style="left:303px;top:291px;width:138px">
    <div class="card-img" role="img" aria-label="Young entrepreneurs in a meeting"></div>
    <div class="card-band" style="background:var(--green)">Entrepreneurs <span>and</span><br>Start-ups</div>
    <p class="body-s" style="margin-top:6px;padding-left:7px">Are you looking for funding?<br>Lorem ipsum dolor sit amet?</p>
  </div>
  <div class="abs" style="left:444px;top:291px;width:132px">
    <div class="card-img" role="img" aria-label="Investors shaking hands" style="border-radius:0 6px 0 0"></div>
    <div class="card-band" style="background:var(--amber)">Investors <span>and</span><br>Business Angels</div>
    <p class="body-s" style="margin-top:6px;padding-left:6px">Are you willing to invest in Innovative projects and become a member?</p>
  </div>
  <div class="abs connect">Connect<br>Now</div>

  <div class="abs hrule" style="top:417px"></div>

  <h2 class="abs sec-h" style="left:161px;top:436px">Portfolio</h2>
  <div class="abs pager" style="left:266px;top:440px"><i>‹</i><i>›</i></div>
  <p class="abs body-s" style="left:162px;top:461px;width:110px">Etiam lectus risus, convallis nec tempus eget, vehicula a lectus.</p>
  <div class="abs more" style="left:162px;top:490px">VIEW MORE</div>
  <div class="abs port-box" style="left:303px">Orvia Labs</div>
  <div class="abs port-box" style="left:371px">Ridgeway Group</div>
  <div class="abs port-box" style="left:443px;background:#f2f2f2">Coverlyn</div>
  <div class="abs port-box" style="left:514px">Palmtrust</div>

  <div class="abs hrule" style="top:524px"></div>

  <h2 class="abs why-h">Why choose <b>Bright Harbor</b>?</h2>

  <div class="abs feature" style="left:163px">
    <div class="icon"><svg width="28" height="24" viewBox="0 0 28 24" fill="#fff"><rect x="11" y="0" width="6" height="6"/><rect x="13.3" y="6" width="1.4" height="5"/><rect x="4" y="10.5" width="20" height="1.4"/><rect x="3.3" y="10.5" width="1.4" height="6"/><rect x="13.3" y="10.5" width="1.4" height="6"/><rect x="23.3" y="10.5" width="1.4" height="6"/><rect x="1" y="16" width="6" height="6"/><rect x="11" y="16" width="6" height="6"/><rect x="21" y="16" width="6" height="6"/></svg></div>
    <h3>Interdum et malesuada</h3>
    <p>Pellentesque fringilla commodo odio ut tempus. In dapibus eros at pretium</p>
  </div>
  <div class="abs feature" style="left:268px">
    <div class="icon"><svg width="30" height="24" viewBox="0 0 30 24" fill="#fff"><circle cx="15" cy="6" r="4.5"/><path d="M7 22c0-6 3.5-9 8-9s8 3 8 9z"/><circle cx="6" cy="8" r="3.2"/><path d="M0 20c0-4.5 2.5-7 6-7 1 0 2 .2 2.8.7C6.8 15.5 6 18 6 20z"/><circle cx="24" cy="8" r="3.2"/><path d="M30 20c0-4.5-2.5-7-6-7-1 0-2 .2-2.8.7 2 1.8 2.8 4.3 2.8 6.3z"/></svg></div>
    <h3>Interdum et malesuada</h3>
    <p>Pellentesque fringilla commodo odio ut tempus. In dapibus eros at pretium</p>
  </div>
  <div class="abs feature" style="left:374px">
    <div class="icon"><svg width="26" height="26" viewBox="0 0 26 26" fill="none" stroke="#fff" stroke-width="3.2" stroke-linecap="round"><circle cx="8" cy="8" r="5"/><path d="M12 12l10 10M17 17l3-3M20 20l3-3"/></svg></div>
    <h3>Interdum et malesuada</h3>
    <p>Pellentesque fringilla commodo odio ut tempus. In dapibus eros at pretium</p>
  </div>
  <div class="abs feature" style="left:479px">
    <div class="icon"><svg width="26" height="22" viewBox="0 0 26 22" fill="#fff"><rect x="0" y="17" width="4" height="5"/><rect x="5.5" y="14" width="4" height="8"/><rect x="11" y="10" width="4" height="12"/><rect x="16.5" y="5" width="4" height="17"/><rect x="22" y="0" width="4" height="22"/></svg></div>
    <h3>Interdum et malesuada</h3>
    <p>Pellentesque fringilla commodo odio ut tempus. In dapibus eros at pretium</p>
  </div>

  <div class="abs cta-shadow"></div>
  <div class="abs cta">
    <div class="btn label">GET STARTED NOW</div>
    <div class="go"><svg width="12" height="12" viewBox="0 0 12 12"><circle cx="6" cy="6" r="5.5" fill="#fff"/><path d="M3 6h5M6 3.6L8.4 6 6 8.4" stroke="#3c4a55" stroke-width="1.4" fill="none"/></svg></div>
  </div>

  <div class="abs hrule" style="top:785px"></div>

  <h2 class="abs" style="left:161px;top:802px;font-size:15px;font-weight:300;color:#777">Recent <b style="font-weight:700">News</b></h2>
  <div class="abs pager" style="left:402px;top:804px"><i>‹</i><i>›</i></div>
  <div class="abs news-img" role="img" aria-label="Team working around a meeting table with laptops"></div>
  <div class="abs news-title">Sed nec velit quis nunc ullamcorper</div>
  <p class="abs body-s" style="left:285px;top:847px;width:150px;font-size:7.5px">Etiam euismod tempor libero et faucibus. Curabitur sit amet mi vel urna viverra congue.</p>

  <h2 class="abs sec-h" style="left:453px;top:802px;font-size:14px">Testimonial</h2>
  <div class="abs pager" style="left:550px;top:804px"><i>‹</i><i>›</i></div>
  <div class="abs bubble">Etiam euismod tempor libero et faucibus. Curabitur sit amet mi vel urna viverra congue pulvinar eget</div>
  <div class="abs author">John Doe , <span>Manager</span></div>

  <footer class="abs footer">
    <p class="copy">© Bright Harbor 2013. All Rights Reserved</p>
    <div class="social" aria-label="Social media links"><span></span><span></span><span></span></div>
  </footer>
</div>

</body>
</html>
```